Brimwave.com fiber optic internet website redesign

We need a new website design for our fiber optic internet company that provides internet, phone, and tv services. It should use the text "Tamberlyn fiber optics", and "Shine brighter on Tamberlyn". The design should use the color blue and the attached logo.
We are a 30 year old internet company who started as a dial up internet provider in our basement. Today we design, build, and maintain our own fiber optic internet network to provide service to residential, business, educational, healthcare, and governmental customers

```html
<!DOCTYPE html>
<html lang="en">
<head>
<meta charset="utf-8">
<title>Brimwave.com – Residential Internet</title>
<link href="https://fonts.googleapis.com/css2?family=Roboto+Condensed:wght@700&family=Poppins:wght@400;500;600&display=swap" rel="stylesheet">
<style>
:root{
  --blue:#1f6fe0;
  --blue-bright:#2a82e4;
  --navy:#0d3c8a;
  --ink:#2b2f36;
  --pale:#eef4fd;
  --pale-2:#e6eefb;
  --row:#dce8fb;
  --footer:#e9f0fd;
  --bar:#a9bbdc;
  --dark:#06101f;
  --white:#fff;
  --col1:#1e4a8c;--col2:#2a5ca8;--col3:#3574c8;--col4:#2a82e4;
}
*{margin:0;padding:0;box-sizing:border-box}
html,body{width:1200px;height:3058px;overflow:hidden}
body{position:relative;font-family:'Poppins',sans-serif;color:var(--ink);background:var(--white)}
.abs{position:absolute}
.heading{font-family:'Roboto Condensed',sans-serif;font-weight:700}

/* header + hero */
.hero{left:0;top:0;width:1200px;height:670px;background:linear-gradient(160deg,#0a1f4a 0%,#1b4f9c 45%,#0c2b63 100%)}
.hero-wave{left:0;top:460px;width:1200px;height:220px}
.brand{left:133px;top:30px;display:flex;align-items:center;gap:12px;color:var(--white)}
.brand-mark{width:48px;height:48px;border-radius:50%;background:var(--white)}
.brand-name{font-size:26px;font-weight:600;line-height:1}
.brand-sub{font-size:11px;font-weight:500;margin-top:2px}
.nav{left:387px;top:45px;display:flex;gap:18px;color:var(--white);font-size:14px;font-weight:500}
.call{left:940px;top:38px;width:147px;height:34px;border-radius:17px;background:var(--blue);color:var(--white);font-size:13px;display:flex;align-items:center;justify-content:center;gap:8px}
.hero-title{left:0;width:1200px;top:238px;text-align:center;color:var(--white);font-size:50px}

/* pricing */
.section-title{left:0;width:1200px;text-align:center;font-size:40px;color:var(--ink)}
.pricing{left:180px;top:807px;width:839px;height:419px}
.col{position:absolute;top:0;height:419px;border-radius:8px;overflow:hidden;background:var(--white);box-shadow:0 4px 14px rgba(20,60,140,.15)}
.col-head{height:98px;color:var(--white);font-family:'Roboto Condensed',sans-serif;font-weight:700;font-size:20px;line-height:1.1;text-align:center;padding-top:20px;clip-path:polygon(0 0,100% 0,100% 62%,50% 96%,0 62%)}
.col.pkg{background:var(--pale-2);box-shadow:none}
.col.pkg .col-head{clip-path:none;color:#2a5ca8;padding-top:30px;background:var(--pale-2)}
.cell{height:53.5px;display:flex;align-items:center;justify-content:center;font-size:14px;font-weight:500;color:#111}
.cell:nth-child(even){background:var(--row)}
.pkg .cell{font-size:21px;font-weight:400;color:#222}
.pkg .cell:nth-child(even){background:#d5e3fa}
.note{left:300px;width:600px;top:1255px;text-align:center;color:var(--navy);font-size:25px;font-weight:600;line-height:37px}

/* includes */
.includes{left:0;top:1447px;width:1200px;height:795px;background:var(--pale)}
.frame-a{left:470px;top:1625px;width:175px;height:175px;border-top:10px solid var(--blue);border-right:10px solid var(--blue);border-top-right-radius:14px}
.frame-b{left:180px;top:1955px;width:176px;height:175px;border-bottom:10px solid var(--blue);border-left:10px solid var(--blue);border-bottom-left-radius:14px}
.photo{left:191px;top:1637px;width:443px;height:483px;border-radius:18px;background:linear-gradient(180deg,#e9edf3 0%,#c7d2e2 55%,#3c5c93 100%)}
.features{left:676px;top:1640px;width:343px;list-style:none;display:flex;flex-direction:column;gap:6px}
.features li{border:1.5px solid var(--blue);border-radius:6px;background:var(--white);color:var(--navy);font-size:12.5px;font-weight:500;line-height:19px;padding:9px 20px}

/* voip */
.voip{left:0;top:2238px;width:1200px;height:480px;background:radial-gradient(ellipse at 30% 40%,#123a5c 0%,#07152a 55%,var(--dark) 100%)}
.voip-title{left:0;width:1200px;top:2335px;text-align:center;color:var(--white);font-size:38px;line-height:46px}
.cta{left:516px;top:2448px;width:167px;height:33px;border:1.5px solid var(--white);border-radius:17px;color:var(--white);font-size:14px;display:flex;align-items:center;justify-content:center}
.voip-wave{left:0;top:2490px;width:1200px;height:240px}

/* footer */
.footer{left:0;top:2700px;width:1200px;height:304px;background:var(--footer)}
.f-brand{left:167px;top:2748px;display:flex;align-items:center;gap:12px;color:var(--navy)}
.f-brand .brand-mark{background:var(--navy);width:46px;height:46px}
.f-about{left:162px;top:2827px;width:310px;font-size:16px;line-height:23px;color:#555}
.f-head{top:2717px;font-size:18px;font-weight:600;color:var(--navy)}
.f-links{left:558px;top:2770px;list-style:none;font-size:16px;color:#555;line-height:37.7px}
.contact-row{left:799px;display:flex;align-items:center;gap:20px;font-size:16px;color:#444}
.icon-box{width:38px;height:38px;border-radius:8px;background:var(--white);border:1px solid #bcd0f3;display:flex;align-items:center;justify-content:center}
.socials{left:803px;top:2902px;display:flex;gap:23px}
.socials span{width:34px;height:34px;border-radius:50%;background:var(--blue)}
.copyright{left:0;top:3004px;width:1200px;height:54px;background:var(--bar);color:var(--white);font-size:15px;text-align:center;line-height:54px}
</style>
</head>
<body>

<div class="abs hero" role="img" aria-label="Photo of a technician with a laptop in a blue-lit server room"></div>
<svg class="abs hero-wave" viewBox="0 0 1200 220" preserveAspectRatio="none">
  <path d="M0 90 C120 200 220 20 330 20 C470 20 520 170 640 170 C790 170 880 40 1000 40 C1100 40 1150 90 1200 80 L1200 220 L0 220Z" fill="var(--blue)" opacity=".85"/>
  <path d="M0 150 C90 210 200 60 330 60 C470 60 540 170 650 170 C800 170 900 80 1020 80 C1110 80 1160 110 1200 90 L1200 220 L0 220Z" fill="var(--blue)"/>
  <path d="M30 200 C140 170 230 95 340 95 C470 95 560 205 690 205 C830 205 930 115 1050 115 C1130 115 1170 130 1200 125 L1200 220 L0 220Z" fill="var(--white)"/>
</svg>

<header>
  <div class="abs brand"><span class="brand-mark"></span><div><div class="brand-name">Brimwave.com</div><div class="brand-sub">Tamberlyn Fiber Optics</div></div></div>
  <nav class="abs nav"><span>Home</span><span>Residential</span><span>Business</span><span>Services</span><span>Telecom</span><span>Contact us</span><span>Users</span></nav>
  <div class="abs call"><svg width="12" height="12" viewBox="0 0 24 24"><path fill="#fff" d="M6.6 10.8a15 15 0 006.6 6.6l2.2-2.2c.3-.3.7-.4 1-.2 1.1.4 2.3.6 3.6.6.6 0 1 .4 1 1V20c0 .6-.4 1-1 1A17 17 0 013 4c0-.6.4-1 1-1h3.5c.6 0 1 .4 1 1 0 1.3.2 2.5.6 3.6.1.3 0 .7-.2 1z"/></svg>1-888-555-0192</div>
</header>
<h1 class="abs heading hero-title">Residential Internet</h1>

<h2 class="abs heading section-title" style="top:718px">Pricing Plans up to 1 Gigabit !!!</h2>

<div class="abs pricing">
  <div class="col pkg" style="left:0;width:166px"><div class="col-head">Package</div>
    <div class="cell">25M</div><div class="cell">50M</div><div class="cell">100M</div><div class="cell">200M</div><div class="cell">500M</div><div class="cell">1000M</div></div>
  <div class="col" style="left:168px;width:166px"><div class="col-head" style="background:var(--col1)">Download<br>Speed</div>
    <div class="cell">25 Mbps</div><div class="cell">50 Mbps</div><div class="cell">100 Mbps</div><div class="cell">200 Mbps</div><div class="cell">500 Mbps</div><div class="cell">1000 Mbps</div></div>
  <div class="col" style="left:336px;width:166px"><div class="col-head" style="background:var(--col2)">Upload Speed</div>
    <div class="cell">10 Mbps</div><div class="cell">15 Mbps</div><div class="cell">25 Mbps</div><div class="cell">50 Mbps</div><div class="cell">75 Mbps</div><div class="cell">100 Mbps</div></div>
  <div class="col" style="left:504px;width:166px"><div class="col-head" style="background:var(--col3)">Monthly Price</div>
    <div class="cell">$55</div><div class="cell">$65</div><div class="cell">$75</div><div class="cell">$85</div><div class="cell">$105</div><div class="cell">$125</div></div>
  <div class="col" style="left:672px;width:167px"><div class="col-head" style="background:var(--col4)">Broadband<br>Label</div>
    <div class="cell">25M Package</div><div class="cell">50M Package</div><div class="cell">100M Package</div><div class="cell">200M Package</div><div class="cell">500M Package</div><div class="cell">1000M Package</div></div>
</div>

<p class="abs note">Speeds up to 10Gb symmetrical are available. If you don't see what package you are looking for please contact us for pricing.</p>

<section>
  <div class="abs includes"></div>
  <h2 class="abs heading section-title" style="top:1527px">Internet Service Includes</h2>
  <div class="abs frame-a"></div>
  <div class="abs frame-b"></div>
  <div class="abs photo" role="img" aria-label="Photo of a lineman in a hard hat working on a utility pole with fiber cables"></div>
  <ul class="abs features">
    <li>High Speed Fiber Optic Internet Connection</li>
    <li>Free Email Addresses</li>
    <li>Unlimited file size on email attachments</li>
    <li>Fast and Friendly LOCAL Phone Support</li>
    <li>Discounted Computer Repair Services</li>
    <li>Free installation and setup</li>
    <li>Price does not include applicable franchise fees or taxes</li>
    <li>If you need more bandwidth you can upgrade at any time!</li>
    <li>The bandwidth limits are not data capped and we will not slow you down or stop your connection if you exceed these limits.</li>
  </ul>
</section>

<section>
  <div class="abs voip" role="img" aria-label="Abstract dark background of glowing network light trails"></div>
  <h2 class="abs heading voip-title">Add VoIP Phone Service for $25/mo OR<br>Bundle with Internet + TV for $15/mo</h2>
  <div class="abs cta">Check Availability</div>
</section>

<footer>
  <div class="abs footer"></div>
  <svg class="abs voip-wave" viewBox="0 0 1200 240" preserveAspectRatio="none">
    <path d="M0 60 C120 -10 260 60 380 120 C500 180 560 210 680 160 C820 100 930 40 1060 60 C1130 70 1170 100 1200 110 L1200 240 L0 240Z" fill="var(--blue)"/>
    <path d="M0 80 C130 20 270 110 390 160 C510 210 590 210 700 170 C830 120 930 70 1050 85 C1120 95 1170 120 1200 130 L1200 240 L0 240Z" fill="var(--blue-bright)"/>
    <path d="M0 100 C140 50 280 140 400 185 C520 230 620 225 720 200 C850 170 940 110 1060 115 C1130 118 1170 140 1200 150 L1200 240 L0 240Z" fill="var(--footer)"/>
  </svg>
  <div class="abs f-brand"><span class="brand-mark"></span><div><div class="brand-name">Brimwave.com</div><div class="brand-sub">Tamberlyn Fiber Optics</div></div></div>
  <p class="abs f-about">Lorem ipsum dolor sit amet, consectetur adipiscing elit, sed do eiusmod tempor incididunt ut labore et dolore magna aliqua. Ut enim ad minim veniam, quis nostrud</p>
  <h3 class="abs f-head" style="left:558px">Quick Links</h3>
  <ul class="abs f-links"><li>Home</li><li>Services</li><li>Our Work</li><li>About us</li><li>Contact Us</li></ul>
  <h3 class="abs f-head" style="left:799px">Contact Info</h3>
  <div class="abs contact-row" style="top:2774px"><span class="icon-box"><svg width="14" height="14" viewBox="0 0 24 24"><path fill="var(--blue)" d="M6.6 10.8a15 15 0 006.6 6.6l2.2-2.2c.3-.3.7-.4 1-.2 1.1.4 2.3.6 3.6.6.6 0 1 .4 1 1V20c0 .6-.4 1-1 1A17 17 0 013 4c0-.6.4-1 1-1h3.5c.6 0 1 .4 1 1 0 1.3.2 2.5.6 3.6.1.3 0 .7-.2 1z"/></svg></span>1-888-555-0192</div>
  <div class="abs contact-row" style="top:2836px"><span class="icon-box"><svg width="14" height="12" viewBox="0 0 24 20"><path fill="var(--blue)" d="M2 2h20v16H2z"/><path d="M2 3l10 7 10-7" stroke="#fff" stroke-width="2" fill="none"/></svg></span>hello@brimwave.com</div>
  <div class="abs socials"><span></span><span></span><span></span></div>
  <div class="abs copyright">Copyright © 2024 Brimwave.com</div>
</footer>

</body>
</html>
```